Video production company website

BrightWave Studios is a video and photography production company serving many Fortune 500 clients traveling to Hawaii and International Destinations. Our primary focus is the Corporate and Incentive group market, and offer both photography and video services. In addition, we also create custom marketing, sales, art, and real estate productions.

Target Market(s)

Corporate Incentive Travel Groups

Industry/Entity Type

Videography

Number of Pages Required

4 page

Requirements
Must have
• see doc with content. This will ultimately be needed to be a wordpress design so we can update ourselves.
Nice to have
• sleek design, professional, cutting edge, modern
Should not have
• too much Hawaii Feel, some ok but we do travel international

```html
<!DOCTYPE html>
<html lang="en">
<head>
<meta charset="utf-8">
<title>BrightWave Studios</title>
<link href="https://fonts.googleapis.com/css2?family=Open+Sans:wght@400;600;700&display=swap" rel="stylesheet">
<style>
:root{
  --blue:#2a4fa8;
  --blue-dark:#1e3c8c;
  --text:#555;
  --white:#fff;
  --line:#c9d3e6;
  --footer-top:#3558b8;
  --footer-bottom:#1f3a94;
}
*{margin:0;padding:0;box-sizing:border-box}
html,body{width:718px;height:1200px;overflow:hidden;background:#fff}
body{font-family:"Open Sans",Arial,sans-serif;color:var(--text);position:relative}
.abs{position:absolute}
/* header */
.brand{left:58px;top:13px;display:flex;align-items:center;gap:6px}
.brand-dot{width:20px;height:20px;border-radius:50%;background:var(--blue)}
.brand-name{font-size:12px;font-weight:700;color:var(--blue);line-height:1.1}
.brand-tag{font-size:6px;color:#555;display:block;font-weight:400}
.nav{top:19px;font-size:7.5px;color:#444}
.nav.active{color:var(--blue)}
.signup{left:587px;top:13px;width:72px;height:22px;background:var(--blue);color:#fff;font-size:9px;font-weight:600;display:flex;align-items:center;justify-content:center;border-radius:2px}
/* hero */
.hero{left:0;top:50px;width:718px;height:257px;background:linear-gradient(180deg,#f2b84a 0%,#f6c35a 35%,#c88a2c 62%,#4a3420 85%,#2a1e14 100%)}
.hero-title{right:59px;top:180px;font-size:29px;font-weight:600;color:#fff}
/* welcome */
.welcome{left:0;width:718px;top:333px;text-align:center;font-size:13.5px;color:var(--blue);font-weight:400}
.intro{left:80px;width:558px;top:367px;text-align:center;font-size:7px;line-height:15.6px;color:#555}
.btn{top:434px;height:27px;font-size:10.5px;display:flex;align-items:center;justify-content:center;border-radius:2px}
.btn-solid{left:262px;width:90px;background:var(--blue);color:#fff}
.btn-line{left:366px;width:90px;border:1.5px solid var(--blue);color:var(--blue)}
.rule{left:58px;top:492px;width:601px;height:1px;background:var(--line)}
/* gallery */
.photo{top:522px;height:148px;border:3px solid #eee;box-shadow:0 1px 4px rgba(0,0,0,.35)}
.photo-left{left:59px;width:287px;background:linear-gradient(180deg,#d49a4c 0%,#6a5a4a 40%,#3a6a8a 75%,#2e4c6a 100%)}
.photo-right{left:371px;width:288px;background:linear-gradient(180deg,#a8c8e0 0%,#6a9a58 45%,#4f8a3c 65%,#2f4fb0 100%)}
.caption{top:689px;width:287px;text-align:center;font-size:9.5px;line-height:17px;color:#555}
.caption a{color:var(--blue);font-weight:600;text-decoration:underline}
/* contact */
.contact{left:0;top:747px;width:718px;height:263px;background:linear-gradient(180deg,#4c4e54 0%,#3a3e46 55%,#2c3038 100%)}
.contact-title{left:0;width:718px;top:778px;text-align:center;color:#fff;font-size:12px;font-weight:600}
.field{border:1px solid rgba(255,255,255,.35);color:#e8e8e8;font-size:8px;padding:0 14px;display:flex;align-items:center;justify-content:space-between}
.field svg{width:14px;height:14px}
.send{left:311px;top:952px;width:96px;height:26px;border:1px solid rgba(255,255,255,.6);color:#fff;font-size:9.5px;display:flex;align-items:center;justify-content:center;border-radius:2px}
/* footer */
.footer{left:0;top:1010px;width:718px;height:190px;background:linear-gradient(180deg,var(--footer-top),var(--footer-bottom))}
.partner{left:58px;top:1062px;display:flex;align-items:center;gap:6px;color:#fff}
.partner-box{width:46px;height:46px;border:3px solid #fff}
.partner-name{font-size:10.5px;font-weight:600;line-height:1.2}
.col-head{top:1030px;color:#fff;font-size:9px;font-weight:600}
.links{top:1051px;list-style:none;color:#fff;font-size:7px;line-height:16.5px}
.links li::before{content:"» ";margin-right:4px}
.info{color:#fff;font-size:7px;line-height:14px}
.social{left:552px;top:1061px;display:flex;gap:7px}
.social span{width:22px;height:22px;border-radius:50%;border:1.5px solid #fff}
.copy{left:0;width:718px;top:1173px;text-align:center;color:#fff;font-size:7px}
</style>
</head>
<body>
<!-- header -->
<div class="abs brand"><span class="brand-dot"></span><span class="brand-name">BrightWave Studios<span class="brand-tag">The Best of the Best</span></span></div>
<span class="abs nav active" style="left:258px">Home</span>
<span class="abs nav" style="left:313px">About us</span>
<span class="abs nav" style="left:377px">Our Service</span>
<span class="abs nav" style="left:451px">Production</span>
<span class="abs nav" style="left:523px">Contact us</span>
<div class="abs signup">Sign up Now</div>

<!-- hero -->
<div class="abs hero" role="img" aria-label="Sunset over the ocean with a palm tree silhouette"></div>
<svg class="abs" style="left:28px;top:170px" width="10" height="16"><path d="M8 2 L2 8 L8 14" stroke="#fff" stroke-opacity=".6" fill="none" stroke-width="1.5"/></svg>
<svg class="abs" style="left:680px;top:170px" width="10" height="16"><path d="M2 2 L8 8 L2 14" stroke="#fff" stroke-opacity=".6" fill="none" stroke-width="1.5"/></svg>
<div class="abs hero-title">The Best of the Best</div>
<svg class="abs" style="left:620px;top:260px" width="32" height="32"><circle cx="16" cy="16" r="14" stroke="#ddd" stroke-width="2" fill="none"/><path d="M12 9 L23 16 L12 23 Z" stroke="#ddd" stroke-width="2" fill="none"/></svg>

<!-- welcome -->
<h1 class="abs welcome">Welcome To BrightWave Studios</h1>
<p class="abs intro">Lorem ipsum dolor sit amet, mel nobis dolorem molestiae in, usu persius eripuit ad. Noster mollis denique at vim, no qui aeterno petentium. Ei insolens vulputate usu, eu sed sempertorquatos intellegam, et graece forensibus usu. Te vis mucius salutatus. An quod enim sensibus sit, eu qui dico posse luptatum. Lorem ipsum dolor sit amet, mel nobis dolorem molestiae in, usu persius eripuit ad. Noster mollis denique at vim, no qui aeterno petentium.</p>
<div class="abs btn btn-solid">Get in Touch</div>
<div class="abs btn btn-line">Read More</div>
<div class="abs rule"></div>

<!-- gallery -->
<div class="abs photo photo-left" role="img" aria-label="Guests at an outdoor dinner event at sunset"></div>
<div class="abs photo photo-right" role="img" aria-label="Group playing lawn games at a beachside event"></div>
<p class="abs caption" style="left:59px">Please contact us for you <a>next project</a> and for a password to watch our sample videos.</p>
<p class="abs caption" style="left:371px">Please <a>contact us</a> for a custom quote.<br>Please <a>click here</a> for our gallery.</p>

<!-- contact -->
<div class="abs contact" role="img" aria-label="Child surfing a small wave, dimmed background"></div>
<h2 class="abs contact-title">CONTACT US</h2>
<div class="abs field" style="left:85px;top:818px;width:270px;height:28px">First &amp; Last name<svg viewBox="0 0 14 14"><circle cx="7" cy="4.5" r="3" fill="#ccc"/><path d="M1 14 C1 9 13 9 13 14Z" fill="#ccc"/></svg></div>
<div class="abs field" style="left:85px;top:857px;width:270px;height:28px">Phone No.<svg viewBox="0 0 14 14"><path d="M3 1 L5 4 L4 6 C5 8 6 9 8 10 L10 9 L13 11 L11 13 C6 12 2 8 1 3 Z" fill="none" stroke="#ccc"/></svg></div>
<div class="abs field" style="left:85px;top:895px;width:270px;height:28px">Email Id *<svg viewBox="0 0 14 14"><rect x="1" y="3" width="12" height="8" fill="none" stroke="#ccc"/><path d="M1 3 L7 8 L13 3" fill="none" stroke="#ccc"/></svg></div>
<div class="abs field" style="left:373px;top:818px;width:270px;height:28px">Company Info</div>
<div class="abs field" style="left:373px;top:857px;width:270px;height:66px;align-items:flex-start;padding-top:6px">your message</div>
<div class="abs send">Send Message</div>

<!-- footer -->
<div class="abs footer"></div>
<div class="abs partner"><span class="partner-box"></span><span class="partner-name">Harborline<br>Property<br>Solutions</span></div>
<h3 class="abs col-head" style="left:196px">MENUS</h3>
<ul class="abs links" style="left:196px"><li>Home</li><li>About us</li><li>Our services</li><li>Blog</li><li>Contact us</li></ul>
<h3 class="abs col-head" style="left:290px">QUICK LINKS</h3>
<ul class="abs links" style="left:290px"><li>Site map</li><li>Terms and Conditions</li><li>Disclaimer</li><li>Privacy Policy</li><li>Contact us</li></ul>
<h3 class="abs col-head" style="left:406px">CONTACT US</h3>
<svg class="abs" style="left:405px;top:1052px" width="10" height="10"><path d="M5 1 L9.5 5 H8 V9 H2 V5 H0.5 Z" fill="#fff"/></svg>
<p class="abs info" style="left:422px;top:1052px">BrightWave Studios, LLC<br>P.O. Box 412-870<br>Lanai HI 96763</p>
<svg class="abs" style="left:407px;top:1102px" width="8" height="11"><rect x="1" y="0.5" width="6" height="10" rx="1" fill="none" stroke="#fff"/></svg>
<p class="abs info" style="left:423px;top:1102px">Call Us : (555)014-2297</p>
<svg class="abs" style="left:405px;top:1127px" width="11" height="9"><rect x=".5" y=".5" width="10" height="8" fill="none" stroke="#fff"/><path d="M.5 .5 L5.5 5 L10.5 .5" fill="none" stroke="#fff"/></svg>
<p class="abs info" style="left:424px;top:1126px">hello@brightwavestudios.example</p>
<h3 class="abs col-head" style="left:552px">CONNECT US WITH</h3>
<div class="abs social"><span></span><span></span><span></span><span></span></div>
<p class="abs copy">© &nbsp;Companyname 2016 . All Rights Reserved</p>
</body>
</html>
```